Packaging Design for Fruit Juice Product

The Product is a fruit juice product. Kindly refer to the photograph attached for the temporary bottle shape and label position. (Please note that the cap colour will be different (not green), as it will be adjusted with the label design)

The fruit is Carica (it's similar like Papaya, but just in yellow color and smaller size). Like the other juice products, the target market covers most of the age range from 10 - 60 years old.

The temporary product name is: KEM

The fact that this juice product is quite unique, I want the product design to be something revolutionary and 'epic'.
The graphic design could be anything depends on your imagination. Basically, I want you to expand your creativity in designing the logo and the overall graphic design for the label.

- Do not design something ordinary or mediocre. Be Extraordinary -

*****The information below may / may not be used to base the label design. It is all up to you to decide whether it is useful in designing the label or not*****

I also have attached the basic information of the fruit and the place where the Carica tree grows: Dieng Plateau.
Dieng Plateau is Highland area where there are mountains. This Dieng Plateau is believed to be the place where the Gods live in the past.
This is probably because of the beautiful landscapes and the epic nature gift such as multi colour lakes, Volcanic crater, etc. (There are lots of myth about this place anyway).
Updates

There are lots of amazing and absolutely great designs on these websites:
You may want to check for the inspiration of our Fruit Juice Project 

Industry/Entity Type

Graphic Design

Requirements
Must have
• Remarkable logo and graphic design.

```html
<!DOCTYPE html>
<html lang="en">
<head>
<meta charset="utf-8">
<title>KEM Carica Juice – Label</title>
<link href="https://fonts.googleapis.com/css2?family=Montserrat:wght@500;600;800&family=Yellowtail&display=swap" rel="stylesheet">
<style>
  :root {
    --night: #050403;
    --ember: #3a2204;
    --gold: #f2c81f;
    --sun: #ffe15a;
    --flame: #ff8a00;
    --neon-red: #ff3b00;
    --label-black: #0b0906;
    --mist: #e9d46a;
  }
  * { margin: 0; padding: 0; box-sizing: border-box; }
  html, body {
    width: 900px;
    height: 1200px;
    overflow: hidden;
  }
  body {
    background: radial-gradient(ellipse 480px 520px at 50% 42%, var(--ember) 0%, var(--night) 72%);
    font-family: "Montserrat", sans-serif;
    position: relative;
  }
  .label {
    position: absolute;
    left: 90px;
    top: 150px;
    width: 720px;
    height: 700px;
    background: var(--label-black);
    overflow: hidden;
    box-shadow: 0 0 120px rgba(255, 160, 20, 0.25);
  }
  .label__scenery {
    position: absolute;
    inset: 0 0 auto 0;
    height: 380px;
    background:
      radial-gradient(ellipse 320px 110px at 60% 42%, rgba(255, 170, 30, 0.55), transparent 70%),
      linear-gradient(180deg, var(--mist) 0%, var(--gold) 38%, #a77a0c 62%, #2a1c05 84%, var(--label-black) 100%);
  }
  .label__content {
    position: absolute;
    left: 0;
    right: 0;
    top: 170px;
    text-align: center;
    color: var(--gold);
  }
  .brand-name {
    font-weight: 800;
    font-size: 190px;
    line-height: 1;
    letter-spacing: 6px;
    color: var(--sun);
  }
  .product-type {
    margin-top: 6px;
    font-weight: 600;
    font-size: 44px;
    letter-spacing: 8px;
    color: var(--flame);
  }
  .label-tagline {
    margin-top: 14px;
    font-family: "Yellowtail", cursive;
    font-size: 52px;
    color: var(--flame);
    text-shadow: 0 0 6px var(--neon-red);
  }
  .benefits {
    margin-top: 26px;
    font-weight: 500;
    font-size: 32px;
    line-height: 1.35;
    color: var(--gold);
  }
  .specs {
    margin-top: 22px;
    font-weight: 500;
    font-size: 19px;
    letter-spacing: 1px;
    color: var(--gold);
  }
  .poster-tagline {
    position: absolute;
    left: 0;
    right: 0;
    top: 1000px;
    text-align: center;
    font-family: "Yellowtail", cursive;
    font-size: 66px;
    color: var(--sun);
    text-shadow: 0 0 4px var(--flame), 0 0 12px var(--neon-red), 0 0 24px var(--neon-red);
  }
</style>
</head>
<body>
  <section class="label">
    <div class="label__scenery" role="img" aria-label="Golden clouds over a dark volcanic mountain of the Dieng Plateau, crossed by a glowing orange ring of light"></div>
    <div class="label__content">
      <h1 class="brand-name">KEM</h1>
      <p class="product-type">CARICA JUICE</p>
      <p class="label-tagline">from the home of the gods</p>
      <p class="benefits">Low in calories.<br>Rich in proteins and fibers.</p>
      <p class="specs">NO ADDED SUGAR • 15 Fl oz (450ml)</p>
    </div>
  </section>
  <p class="poster-tagline">from the home of the gods</p>
</body>
</html>
```